Energieberatung sucht Corporate Design
Zielgruppe
Ich führe Energieberatungen für Immobilieneigentümer durch, erstelle Sanierungsvorschläge sowie Förderanträge. Für Verkäufer und Vermieter fertige ich Energieausweise an, um die energetisch Qualität des Gebäudes darzustellen.
Energieberatung soll für die Kunden ein Wegweiser für modernes, klimaneutrales und kostengünstiges Wohnen sein.
Meine Zielgruppe sind Immobilieneigentümer, Verkäufer und Vermieter von Immobilien sowie Käufer von Immobilien.
Aufgabenstellung
Ich suche ein hochwertiges Design, welches modern und zeitlos ist, aber auch die energetische Komponente berücksichtigt. Mit dem Design soll das verstaubte Image der Energieberatung abgelegt werden. Die Kunden sollen damit zukunftsorientiertes, modernes Wohnen, Wohnqualität und Kostenersparnis verbinden.

```html
<!DOCTYPE html>
<html lang="de">
<head>
<meta charset="utf-8">
<title>Energieberatung Lena Harwig – Corporate Design</title>
<link href="https://fonts.googleapis.com/css2?family=Source+Sans+3:wght@400;600;700&display=swap" rel="stylesheet">
<style>
:root{
  --stage:#cdd0d4;
  --paper:#ffffff;
  --paper-grey:#e8e8e7;
  --teal:#117b97;
  --lime:#c4be12;
  --yellow:#e2d100;
  --ink:#4d4d4d;
  --copy:#9a9a9a;
  --fold:#c9c9c9;
  --gradient:linear-gradient(90deg,var(--teal),var(--yellow));
}
*{box-sizing:border-box;margin:0;padding:0}
html,body{width:999px;height:1200px;overflow:hidden}
body{background:var(--stage);font-family:"Source Sans 3",sans-serif;position:relative;color:var(--ink)}
.sheet{position:absolute;background:var(--paper);box-shadow:3px 4px 8px rgba(0,0,0,.28)}

/* brand wordmark */
.brand{display:flex;align-items:center;gap:.45em;color:var(--teal);font-weight:600;line-height:1.05}
.brand-square{width:1.9em;height:1.9em;background:var(--teal);flex:none}
.brand-name span{display:block}
.brand--mono{color:#111}.brand--mono .brand-square{background:#111}

/* logo card */
.logo-card{left:362px;top:28px;width:582px;height:263px;display:flex;align-items:center;justify-content:center}
.logo-card .brand{font-size:28px}

/* business cards */
.card{width:235px;height:153px}
.card-front{left:56px;top:340px}
.card-front .brand{position:absolute;left:16px;top:14px;font-size:12.5px}
.card-person{position:absolute;left:16px;top:74px;font-size:7px;color:#333}
.card-person b{color:var(--teal)}
.card-address{position:absolute;left:16px;top:117px;font-size:6.8px;line-height:10px;color:#333}
.card-contact{position:absolute;left:118px;top:98px;height:46px;border-left:1px solid var(--teal);padding-left:9px}
.card-band{position:absolute;left:0;right:0;bottom:0;height:8px;background:var(--lime);clip-path:polygon(0 100%,3% 0,97% 0,100% 100%)}
.card-back{left:56px;top:508px;background:var(--teal);display:flex;flex-direction:column;align-items:center;justify-content:center;gap:10px}
.card-back .brand{color:var(--lime);font-size:13px}.card-back .brand-square{background:var(--lime)}
.card-back-url{color:#fff;font-size:7px;font-weight:600}
.card-grey{left:55px;top:697px;background:var(--paper-grey);display:flex;align-items:center;justify-content:center}
.card-mono{left:55px;top:866px;display:flex;align-items:center;justify-content:center}
.card-grey .brand,.card-mono .brand{font-size:15px}

/* contact list */
.contact{list-style:none;font-size:6.8px;line-height:10px;color:var(--teal)}
.contact li{display:flex;align-items:center;gap:4px}
.contact svg{width:7px;height:7px;fill:var(--teal);flex:none}

/* letterhead */
.letter{left:364px;top:340px;width:580px;height:820px;overflow:hidden}
.letter-band-top{position:absolute;left:0;right:0;top:0;height:15px;background:var(--gradient);clip-path:polygon(0 0,100% 0,97.5% 100%,2.5% 100%)}
.letter-band-bottom{position:absolute;left:0;right:0;bottom:0;height:14px;background:var(--teal);clip-path:polygon(2% 0,98% 0,100% 100%,0 100%)}
.letter .brand{position:absolute;left:59px;top:42px;font-size:19px}
.letter-contact{position:absolute;left:445px;top:50px;border-left:1px solid var(--lime);padding:2px 0 2px 9px}
.letter-contact .contact{font-size:7px}
.sender-line{position:absolute;left:59px;top:124px;font-size:6.8px;font-weight:600;color:var(--teal)}
.recipient{position:absolute;left:59px;top:146px;font-size:11px;line-height:14px;color:var(--copy)}
.subject{position:absolute;left:59px;top:248px;font-size:11px;color:var(--copy)}
.letter-body{position:absolute;left:59px;top:285px;width:470px;font-size:10.6px;line-height:14px;color:var(--copy)}
.letter-body p{margin-bottom:14px}
.fold{position:absolute;left:0;height:1px;background:var(--fold)}
.watermark{position:absolute;left:194px;top:540px;width:198px;height:198px;border:7px solid #f1f1f3}
.letter-footer{position:absolute;left:59px;top:774px;right:20px;display:flex;font-size:6.6px;line-height:10.5px;color:#333}
.footer-col{padding-right:12px;margin-right:12px;border-right:1px solid var(--lime)}
.footer-col:last-child{border:0;margin:0;padding:0}
.footer-col b{color:var(--teal);font-weight:700}
.letter-footer .contact{color:#333;font-size:6.6px;line-height:10.5px}
</style>
</head>
<body>
<svg width="0" height="0" style="position:absolute">
  <defs>
    <symbol id="ico-phone" viewBox="0 0 10 10"><path d="M2 0.5 3.6 2.6 2.8 3.6Q3.8 5.9 6.4 7.2L7.4 6.4 9.5 8 8.6 9.5Q1 8.6 0.5 1.4Z"/></symbol>
    <symbol id="ico-fax" viewBox="0 0 10 10"><path d="M2.5 0h4l1 1v2.5h-5zM0.5 4h9v4h-1.5V6.5h-5V8H0.5zM3 7h4v3H3z"/></symbol>
    <symbol id="ico-mail" viewBox="0 0 10 10"><path d="M0.5 2h9v6h-9zM1.2 2.6 5 5.6 8.8 2.6"/></symbol>
    <symbol id="ico-web" viewBox="0 0 10 10"><path d="M5 0.5a4.5 4.5 0 1 0 0.01 0zM5 1.5c-1 1-1.4 2.2-1.4 3.5S4 7.5 5 8.5c1-1 1.4-2.2 1.4-3.5S6 2.5 5 1.5zM1.3 4.5h7.4v1H1.3z"/></symbol>
  </defs>
</svg>

<section class="sheet logo-card">
  <div class="brand"><i class="brand-square"></i><div class="brand-name"><span>Energieberatung</span><span>Lena Harwig</span></div></div>
</section>

<section class="sheet card card-front">
  <div class="brand"><i class="brand-square"></i><div class="brand-name"><span>Energieberatung</span><span>Lena Harwig</span></div></div>
  <p class="card-person"><b>Lena Harwig</b> - Geschäftsleitung</p>
  <p class="card-address">Musterstraße 126<br>00000 Musterstadt</p>
  <div class="card-contact">
    <ul class="contact">
      <li><svg><use href="#ico-phone"/></svg>+49 1234-56789-0</li>
      <li><svg><use href="#ico-fax"/></svg>+49 1234-56789-1</li>
      <li><svg><use href="#ico-mail"/></svg>info@muster.com</li>
      <li><svg><use href="#ico-web"/></svg>www.muster.com</li>
    </ul>
  </div>
  <div class="card-band"></div>
</section>

<section class="sheet card card-back">
  <div class="brand"><i class="brand-square"></i><div class="brand-name"><span>Energieberatung</span><span>Lena Harwig</span></div></div>
  <p class="card-back-url">www.muster.com</p>
</section>

<section class="sheet card card-grey">
  <div class="brand"><i class="brand-square"></i><div class="brand-name"><span>Energieberatung</span><span>Lena Harwig</span></div></div>
</section>

<section class="sheet card card-mono">
  <div class="brand brand--mono"><i class="brand-square"></i><div class="brand-name"><span>Energieberatung</span><span>Lena Harwig</span></div></div>
</section>

<article class="sheet letter">
  <div class="letter-band-top"></div>
  <div class="watermark"></div>
  <div class="brand"><i class="brand-square"></i><div class="brand-name"><span>Energieberatung</span><span>Lena Harwig</span></div></div>
  <div class="letter-contact">
    <ul class="contact">
      <li><svg><use href="#ico-phone"/></svg>+49 1234-56789-0</li>
      <li><svg><use href="#ico-fax"/></svg>+49 1234-56789-1</li>
      <li><svg><use href="#ico-mail"/></svg>info@muster.com</li>
      <li><svg><use href="#ico-web"/></svg>www.muster.com</li>
    </ul>
  </div>
  <p class="sender-line">Energieberatung Lena Harwig - Postfach 0000 - 00000 Musterstadt</p>
  <address class="recipient" style="font-style:normal">Firma Berger und Partner<br>Herr Berger<br>Lindenweg 45<br>44789 Bochum<br>Deutschland</address>
  <p class="subject">Betreffzeile</p>
  <div class="fold" style="top:350px;width:20px"></div>
  <div class="fold" style="top:521px;width:28px"></div>
  <div class="fold" style="top:643px;width:20px"></div>
  <div class="letter-body">
    <p>Sehr geehrte Damen und Herren,</p>
    <p>schön, dass Sie neugierig reinschauen, obwohl hier ja eigentlich noch gar kein richtiger Text steht, sondern nur der sogenannte Blindtext. Dieser Blindtext will Ihnen nämlich sagen: Erstens will er den Texter entschuldigen – tut uns leid, aber es war einfach unmöglich, das Ding gestern Nacht noch exakt auf Länge runterzuschreiben. Das Briefing, Sie wissen schon. Schwieriges Thema. Und die Freundin ist krank, und der Freund wollte in diesen neuen Film. Und dann hat sich der Film so überhaupt nicht gelohnt, sagte er.</p>
    <p>Ja, und zweitens haben wir Sie bis hierhin zum Lesen gebracht und wollen damit belegen, dass nicht alle Marktforscher und Kaffeesatzleser recht haben, die sagen, dass unser armer Freund Otto Normalverbraucher und seine hässliche Schwester Lieschen Müller maximal Null Komma gar kein Interesse haben für Texte.</p>
    <p>Drittens sollten wir für ein paar Zeilen abschweifen und uns dem Gegenstand unserer Bemühungen zuwenden. Was heißt überhaupt Blindtext? Macht er blind, und wenn ja, wen? Ich denke, das Wörtchen will uns ja auch nur warnend darauf hinweisen, dass viel zu oft nach dem Motto „Augen zu und durch“ verfahren wird bei der verantwortungsvollen Aufgabe, Grauwert zu verteilen.</p>
    <p>Erstens will er den Texter entschuldigen – tut uns leid, aber es war einfach unmöglich, das Ding gestern Nacht noch exakt auf Länge runterzuschreiben. Das Briefing, Sie wissen schon. Schwieriges Thema. Und die Freundin ist krank, und der Freund wollte in diesen neuen Film. Und dann hat sich der Film so überhaupt nicht gelohnt, sagte er.</p>
    <p>Mit freundlichen Grüßen,</p>
    <p>Clara Beispiel</p>
  </div>
  <footer class="letter-footer">
    <div class="footer-col"><b>Energieberatung Lena Harwig</b><br>Musterstraße 126<br>00000 Musterstadt</div>
    <div class="footer-col"><b>Geschäftsführer</b><br>Lena Harwig<br>Energieberaterin</div>
    <div class="footer-col">
      <ul class="contact">
        <li><svg><use href="#ico-phone"/></svg>+49 1234-56789-0</li>
        <li><svg><use href="#ico-fax"/></svg>+49 1234-56789-1</li>
        <li><svg><use href="#ico-web"/></svg>www.muster.com</li>
      </ul>
    </div>
    <div class="footer-col"><b>Amtsgericht Stadt</b><br>ABC 0000XX<br>UST-ID DE 000XX</div>
    <div class="footer-col"><b>Bankverbindung ABC</b><br>IBAN DE12 3456 7890 1234 5678<br>BIC ABCDEF12345</div>
  </footer>
  <div class="letter-band-bottom"></div>
</article>
</body>
</html>
```